Looking to design a new sign for our church.

Looking for a new sign
4 x 8 feet dimension
We are renaming the church "Medlow Ridge Community Church"
looking for legible graphics
Would like some type of backdrop being a family tree (oak) / open to other ideas as you are led
I have included a pic of the old sign for your review
would like to incorporate our ministry logo on the lower right hand corner of the sign / see file attached

```html
<!DOCTYPE html>
<html lang="en">
<head>
<meta charset="utf-8">
<title>Medlow Ridge Community Church – Sign</title>
<link href="https://fonts.googleapis.com/css2?family=Montserrat:wght@500;600&display=swap" rel="stylesheet">
<style>
  :root {
    --navy: #050566;
    --shadow-grey: #76767d;
    --leaf-green: #a5b83a;
    --bark-brown: #5f4a1e;
    --ink: #111111;
    --paper: #ffffff;
  }
  html, body {
    margin: 0;
    padding: 0;
    width: 1200px;
    height: 1200px;
    overflow: hidden;
    background: var(--paper);
  }
  .sign {
    display: block;
    width: 1200px;
    height: 1200px;
    font-family: "Montserrat", sans-serif;
  }
  .church-name {
    font-size: 30px;
    font-weight: 500;
    fill: var(--navy);
  }
  .schedule-time { fill: var(--ink); font-size: 24px; font-weight: 500; }
  .schedule-event { fill: var(--navy); font-size: 24px; font-weight: 500; }
  .address-text { fill: var(--paper); font-size: 26px; font-weight: 500; }
  .ministry-name { fill: var(--navy); font-size: 15px; font-weight: 600; }
</style>
</head>
<body>
<svg class="sign" viewBox="0 0 1200 1200" xmlns="http://www.w3.org/2000/svg">
  <defs>
    <radialGradient id="tree-tones" cx="50%" cy="40%" r="60%">
      <stop offset="0%" stop-color="#a5b83a"/>
      <stop offset="55%" stop-color="#3b3f7a"/>
      <stop offset="100%" stop-color="#5f4a1e"/>
    </radialGradient>
    <path id="name-arc" d="M 358 563 A 254 254 0 0 1 848 563"/>
  </defs>

  <!-- header band with curved lower edge -->
  <path class="header-shadow" d="M0 300 H1200 V463 Q900 326 615 322 Q300 320 0 462 Z" fill="var(--shadow-grey)"/>
  <path class="header-band" d="M0 300 H1200 V456 Q900 322 615 318 Q300 316 0 455 Z" fill="var(--navy)"/>

  <!-- curved church name -->
  <text class="church-name">
    <textPath href="#name-arc" startOffset="0" textLength="665" lengthAdjust="spacing">MEDLOW RIDGE COMMUNITY CHURCH</textPath>
  </text>

  <!-- tree artwork area -->
  <circle class="tree-art" cx="600" cy="612" r="212" fill="url(#tree-tones)" role="img" aria-label="Oak family tree with navy and green leaves and spreading roots"/>

  <!-- service schedule -->
  <g class="schedule">
    <text class="schedule-time" x="32" y="722">10:30am</text>
    <text class="schedule-time" x="142" y="722">-</text>
    <text class="schedule-event" x="160" y="722">Worship Service</text>

    <text class="schedule-time" x="32" y="756">9:30am</text>
    <text class="schedule-time" x="142" y="756">-</text>
    <text class="schedule-event" x="162" y="756">Sunday School</text>

    <text class="schedule-time" x="32" y="790">6:00pm</text>
    <text class="schedule-time" x="142" y="790">-</text>
    <text class="schedule-event" x="160" y="790">Wednesday Service</text>
  </g>

  <!-- ministry name, lower right -->
  <g class="ministry">
    <circle cx="1031" cy="762" r="30" fill="none" stroke="var(--navy)" stroke-width="2"/>
    <text class="ministry-name" x="1031" y="814" text-anchor="middle">Kindred Fellowship</text>
  </g>

  <!-- address bar -->
  <rect class="address-bar" x="0" y="837" width="1200" height="37" fill="var(--leaf-green)"/>
  <g class="pin-icon" fill="var(--paper)">
    <path d="M168 843 a9 9 0 0 1 9 9 c0 7 -9 16 -9 16 s-9 -9 -9 -16 a9 9 0 0 1 9 -9 z"/>
    <circle cx="168" cy="852" r="3.2" fill="var(--leaf-green)"/>
  </g>
  <text class="address-text" x="196" y="865">2290 Medlow Ridge Rd, Cedar Hollow, TN, United States, Tennessee</text>
</svg>
</body>
</html>
```